Crowdsourced IT recruitment agency - velmorix

We need an engaging and smart website design for VELMORIX Crowd recruitment. We are young innovative IT recruitment company. We have deep expertise in all IT & digital areas and using crowdsourcing to search the best market candidates faster than ever.
Our mission: to connect people and organizations interests, inspiring each other and enabling together reach better results.

We would like the design to be personalized, emotional, yet simple and neat. It should focus on the person with a problem which we solve.

Reading the site customers should feel safe and confident that velmorix is the trusted partner and everything we do is a quality product.

We also focus on long term relationship with our clients.

We have 4 products:
IT Recruitment – professional recruitment of candidates in IT and digital areas
IT RPO – candidates research process outsourcing(RPO) - provision of resume pools for the client
Kestrel Talent School – training, seminars and networking events for HR professionals from IT and hi-tech companies
Plumview Board – a tool for data visualization in nice and interactive dashboards. It pulls data from different corporate sources (SAP, Oracle, excel, etc.). It looks like a dashboard, on which there are several graphs or diagrams with HR and business KPIs(key performance indicators)

We like material design sites but also open for other options/ideas

Current site velmorix-hire.ru

Examples of websites that we like:
http://www.quobrant.ru
https://dunmirecardio.ru

Site structure:
About us (description, mission, team, clients, office)
Products: Plumview Board, HR IPO, It Recruitment
Kestrel Talent School (list of events (past and future) with the ability to upload photos, descriptions, etc.)
News: Publications, Articles, Blog
Contacts

Industry/Entity Type

Consulting

Number of Pages Required

5+ page

Font styles to use
Serif
Sans Serif

Requirements
Must have
• Individual blocks with the transition to a separate page for each product
• Link to social network (fb, link),
• Subscribe to news on the main page
• Feedback form
• Site structure:
• About us (description, mission, team, clients, office)
• Products: Plumview Board, HR IPO, It Recruitment
• Kestrel Talent School (list of events (past and future) with the ability to upload photos, descriptions, etc.)
• News: Publications, Articles, Blog, Calendars
• Contacts
Should not have
• too crowded
• too complicatied
• without advertising banners
• crammed

```html
<!DOCTYPE html>
<html lang="en">
<head>
<meta charset="utf-8">
<title>VELMORIX Crowd Recruitment</title>
<link href="https://fonts.googleapis.com/css2?family=Open+Sans:wght@400;600;700;800&family=Roboto+Condensed:wght@400;700&display=swap" rel="stylesheet">
<style>
:root{
  --blue:#1a6fc4;
  --blue-dark:#0f4f96;
  --navy:#0c2340;
  --navy-2:#13335a;
  --ink:#222;
  --muted:#555;
  --light:#eef3f9;
  --pale:#e3ecf6;
  --purple:#6a3d9e;
  --green:#5b8b1f;
  --orange:#f2a900;
  --dark:#2b2b2b;
  --white:#fff;
}
*{box-sizing:border-box;margin:0;padding:0}
html,body{width:1200px;height:3303px;overflow:hidden}
body{position:relative;font-family:"Open Sans",Arial,sans-serif;color:var(--ink);background:#f4f4f4}
.btn{display:inline-block;background:var(--blue);color:#fff;font-size:11px;font-weight:700;text-transform:uppercase;padding:8px 12px;letter-spacing:.3px}
.btn::after{content:" \25B8"}
.photo{position:absolute}

/* header */
.site-header{position:absolute;left:0;top:0;width:1200px;height:106px;background:linear-gradient(#fff,#ececec);box-shadow:0 2px 6px rgba(0,0,0,.15);z-index:3}
.brand{position:absolute;left:73px;top:24px;display:flex;align-items:center;gap:12px}
.brand-dot{width:56px;height:56px;border-radius:50%;background:var(--blue)}
.brand-name{font-size:32px;font-weight:700;color:var(--navy)}
.main-nav{position:absolute;left:394px;top:40px;display:flex;gap:48px;font-size:16px;font-weight:600;color:#222}
.auth{position:absolute;left:960px;top:33px;display:flex;gap:14px;align-items:center}
.auth .login{color:var(--blue);font-weight:700;font-size:15px;padding:8px 6px}
.auth .register{background:var(--blue);color:#fff;font-weight:700;font-size:15px;padding:8px 16px}

/* hero */
.hero{position:absolute;left:0;top:106px;width:1200px;height:544px;background:linear-gradient(100deg,#3a4a5c 0%,#6d7f93 35%,#9aa9b6 55%,#5b3440 80%,#8f2336 100%)}
.hero-title{position:absolute;left:62px;top:238px;background:rgba(16,72,150,.9);color:#fff;font-family:"Roboto Condensed",Arial,sans-serif;font-weight:700;font-size:46px;padding:4px 14px;line-height:1.1}
.hero-sub{position:absolute;left:64px;top:314px;color:#fff;font-size:23px}
.hero-text{position:absolute;left:64px;top:352px;width:520px;color:#fff;font-size:16px;line-height:1.4}

/* welcome */
.welcome{position:absolute;left:0;top:650px;width:1200px;height:358px;background:linear-gradient(90deg,#f1f3fa 0%,#f1f3fa 36%,#cfd6e6 60%,#b4bed3 100%)}
.welcome-kicker{position:absolute;left:120px;top:52px;font-size:14px;font-weight:700;color:var(--navy)}
.welcome-mark{position:absolute;left:73px;top:52px;width:36px;height:36px;border-radius:50%;background:var(--blue)}
.welcome-title{position:absolute;left:120px;top:70px;font-size:24px;font-weight:700;color:var(--blue)}
.welcome-text{position:absolute;left:73px;top:116px;width:370px;font-size:14px;line-height:1.65;color:#333}
.welcome .btn{position:absolute;left:73px;top:286px}
.mission{position:absolute;z-index:2;left:704px;top:762px;width:422px;height:266px;background:rgba(18,80,170,.95);color:#fff;padding:24px 36px;box-shadow:0 4px 10px rgba(0,0,0,.3)}
.mission h3{font-size:15px;font-weight:700;margin:22px 0 8px}
.mission p{font-size:21px;line-height:1.45}

/* products */
.products{position:absolute;left:0;top:1008px;width:1200px;height:512px;background:linear-gradient(#dbe5f1,#f4f6f9 60%,#fff)}
.products-photo{left:73px;top:62px;width:1054px;height:410px;background:linear-gradient(90deg,#8b8f99,#c9c0b6 40%,#e6e2dc 55%,#56616f 80%,#2f3a48)}
.section-tab{position:absolute;background:var(--blue-dark);color:#fff;font-weight:700;font-size:20px;padding:6px 12px}
.products .section-tab{left:158px;top:42px}
.product-card{position:absolute;top:218px;width:214px;height:250px;background:#fff;padding:16px 16px}
.product-card svg{width:52px;height:52px}
.product-card h4{font-size:16px;font-weight:700;color:var(--blue);margin:10px 0 18px}
.product-card p{font-size:13px;line-height:1.55;color:#444;height:66px}
.product-card .btn{margin-top:12px}

/* events */
.events{position:absolute;left:73px;top:1530px;width:518px}
.events h2{font-size:20px;font-weight:700;display:flex;align-items:center;gap:10px;color:#111}
.event{display:flex;gap:18px;margin-top:26px;padding-bottom:18px;border-bottom:1px solid #ddd}
.event-photo{width:154px;height:96px;flex:none}
.event small{font-size:12px;color:#444}
.event h5{font-size:14px;font-weight:700;margin:2px 0 8px}
.event p{font-size:12.5px;color:#555;line-height:1.55}
.events .btn{margin-top:24px}

.agency{position:absolute;left:616px;top:1536px;width:512px;height:486px;background:var(--pale)}
.agency-head{background:var(--blue-dark);color:#fff;font-size:20px;font-weight:700;padding:14px 28px;line-height:1.25}
.agency-lead{font-size:12.5px;color:#444;padding:14px 28px;line-height:1.55}
.feature{position:absolute;width:226px;height:144px;background:#fff;text-align:center;padding-top:18px}
.feature svg{width:40px;height:40px}
.feature h6{font-size:15px;font-weight:700;color:var(--blue);margin:6px 0 4px}
.feature p{font-size:12px;color:#555;line-height:1.4;padding:0 12px}

/* video */
.how{position:absolute;left:0;top:2070px;width:1200px;height:363px;background:linear-gradient(#2f3236,#1e2023)}
.how-frame{position:absolute;left:73px;top:48px;width:1008px;height:272px;border:2px solid var(--blue)}
.how-mark{position:absolute;left:312px;top:96px;width:60px;height:60px;border-radius:50%;background:var(--blue)}
.how h2{position:absolute;left:73px;top:170px;width:540px;text-align:center;color:#fff;font-size:32px;font-weight:700}
.how p{position:absolute;left:120px;top:216px;width:446px;text-align:center;color:#fff;font-size:16px;line-height:1.45}
.video-back{position:absolute;left:635px;top:32px;width:450px;height:290px;background:var(--blue)}
.video{left:612px;top:44px;width:452px;height:280px;background:linear-gradient(90deg,#7e8a92,#c9cfd3 50%,#9aa3ab)}
.play{position:absolute;left:800px;top:148px;width:76px;height:76px;border:4px solid #fff;border-radius:50%}
.play::after{content:"";position:absolute;left:26px;top:18px;border-left:26px solid #fff;border-top:16px solid transparent;border-bottom:16px solid transparent}

/* testimonials and blog */
.lower{position:absolute;left:0;top:2433px;width:1200px;height:495px;background:#e9e9e9}
.panel-head{position:absolute;height:42px;color:#fff;font-size:20px;font-weight:700;padding:8px 14px;display:flex;align-items:center;gap:10px}
.panel-head .more{position:absolute;right:14px;top:8px;background:#111;color:#fff;font-size:11px;padding:6px 12px;font-weight:700}
.panel-head .more::after{content:" \25B8"}
.testi-photo{left:73px;top:94px;width:514px;height:340px;background:linear-gradient(90deg,#cfd3d8,#c4b9ad 60%,#8b7566)}
.quote{position:absolute;left:100px;top:116px;width:360px;height:278px;background:#fff;box-shadow:0 2px 8px rgba(0,0,0,.2);text-align:center;padding:14px 40px}
.quote .mark{font-size:40px;font-weight:800;line-height:1}
.quote p{font-size:12.5px;line-height:1.6;color:#333}
.quote b{display:block;margin-top:12px;font-size:15px}
.arrow{position:absolute;top:236px;width:22px;height:22px;border:1px solid #888;border-radius:50%;background:#fff;font-size:12px;text-align:center;line-height:20px;color:#555}
.blog{position:absolute;left:617px;top:86px;width:510px;height:352px;background:#fff}
.post{display:flex;gap:20px;padding:14px 20px 0 22px;height:108px}
.post-photo{width:118px;height:80px;flex:none}
.post small{font-size:12px;color:#333}
.post h5{font-size:15px;font-weight:700;line-height:1.45;margin-top:2px}

/* footer */
.site-footer{position:absolute;left:0;top:2928px;width:1200px;height:375px;background:var(--navy);color:#fff}
.col-title{position:absolute;top:18px;font-size:14px;font-weight:700}
.links{position:absolute;left:73px;top:58px;font-size:13px;line-height:25px;list-style:none}
.contact{position:absolute;left:204px;top:58px;width:200px;font-size:13px;line-height:22px}
.newsletter{position:absolute;left:478px;top:58px;width:290px;font-size:13px;line-height:19px}
.field{width:286px;height:38px;background:#fff;color:#888;font-size:13px;padding:10px 12px;margin-bottom:10px}
.subscribe{display:inline-block;background:var(--orange);color:#111;font-weight:700;font-size:13px;padding:8px 24px}
.follow{position:absolute;left:478px;top:306px;display:flex;align-items:center;gap:10px;font-size:13px;font-weight:700}
.follow span.circle{width:28px;height:28px;border:1px solid #fff;border-radius:50%}
.foot-brand{position:absolute;left:73px;top:240px;display:flex;align-items:center;gap:10px}
.foot-brand .brand-dot{width:44px;height:44px}
.foot-brand .brand-name{color:#fff;font-size:24px}
.copy{position:absolute;left:73px;top:318px;font-size:12px;line-height:20px}
.feedback{position:absolute;left:796px;top:-6px;width:332px;height:352px;background:var(--navy-2);border:2px solid #2a5a96;padding:100px 26px 0}
.feedback-tab{position:absolute;left:12px;top:16px;width:50px;height:64px;background:var(--blue)}
.feedback h3{position:absolute;left:78px;top:40px;font-size:20px;font-weight:700}
.feedback .field{width:276px}
.feedback .message{height:92px}
.feedback .send{display:block;background:var(--orange);color:#111;text-align:center;font-weight:700;font-size:13px;padding:10px}
</style>
</head>
<body>

<header class="site-header">
  <div class="brand"><span class="brand-dot"></span><span class="brand-name">velmorix</span></div>
  <nav class="main-nav"><span>Home</span><span>About Us</span><span>Products</span><span>News</span><span>Contacts</span></nav>
  <div class="auth"><span class="login">LOG IN</span><span class="register">REGISTER</span></div>
</header>

<section class="hero" role="img" aria-label="Photo of two businessmen shaking hands in an office">
  <h1 class="hero-title">Get Your Perfect IT Candidates</h1>
  <p class="hero-sub">More Recruiters. Better Candidates. Lower Costs.</p>
  <p class="hero-text">Hiring has never been easier. Staff your teams faster with the first crowdsourced IT recruitment agency. Over 150 professional recruiters ready to work on your project. Welcome to velmorix!</p>
</section>

<section class="welcome" role="img" aria-label="Photo of two businesswomen sitting on a purple sofa in a bright office">
  <span class="welcome-mark"></span>
  <p class="welcome-kicker">WELCOME TO</p>
  <h2 class="welcome-title">VELMORIX CROWD RECRUITMENT</h2>
  <p class="welcome-text">Lorem ipsum dolor sit amet, consectetur adipiscing elit, sed do eiusmod tempor incididunt ut labore et dolore magna aliqua. Ut enim ad minim veniam, quis nostrud exercitation ullamco laboris nisi ut aliquip ex ea commodo consequat. Duis aute irure dolor in reprehenderit in voluptate velit esse.</p>
  <span class="btn">Read more</span>
</section>

<section class="products">
  <div class="photo products-photo" role="img" aria-label="Photo of smiling women in a meeting"></div>
  <h2 class="section-tab">OUR PRODUCTS</h2>
  <article class="product-card" style="left:161px">
    <svg viewBox="0 0 48 48" fill="none" stroke="var(--blue)" stroke-width="2"><circle cx="20" cy="20" r="13"/><path d="M30 30l12 12"/><circle cx="20" cy="16" r="4" stroke="var(--navy)"/><path d="M12 27c2-5 14-5 16 0" stroke="var(--navy)"/></svg>
    <h4>IT Recruitment</h4>
    <p>Professional recruitment of candidates in IT and digital areas...</p>
    <span class="btn">Read more</span>
  </article>
  <article class="product-card" style="left:381px">
    <svg viewBox="0 0 48 48" fill="none" stroke="var(--blue)" stroke-width="2"><path d="M12 34a9 9 0 010-18 12 12 0 0123 2 8 8 0 011 16z"/><path d="M24 22v14M19 31l5 5 5-5" stroke="var(--navy)"/></svg>
    <h4>IT RPO</h4>
    <p>Candidates research process outsourcing(RPO) - provision of resume...</p>
    <span class="btn">Read more</span>
  </article>
  <article class="product-card" style="left:601px">
    <svg viewBox="0 0 48 48" fill="none" stroke="var(--blue)" stroke-width="2"><circle cx="24" cy="10" r="5"/><circle cx="10" cy="22" r="4"/><circle cx="38" cy="22" r="4"/><path d="M16 40V24h16v16M4 38c0-6 12-6 12 0M32 38c0-6 12-6 12 0" stroke="var(--navy)"/></svg>
    <h4>Kestrel Talent School</h4>
    <p>training, seminars and networking events for HR professionals from IT...</p>
    <span class="btn">Read more</span>
  </article>
  <article class="product-card" style="left:821px">
    <svg viewBox="0 0 48 48" fill="none" stroke="var(--blue)" stroke-width="2"><rect x="6" y="6" width="30" height="36" rx="2"/><path d="M12 34v-8M18 34v-12M24 34v-6" stroke="var(--navy)"/><path d="M12 14h18M12 19h12"/><rect x="32" y="4" width="12" height="16" stroke="var(--navy)"/></svg>
    <h4>Plumview Board</h4>
    <p>A tool for data visualization in nice and interactive dashboards...</p>
    <span class="btn">Read more</span>
  </article>
</section>

<aside class="mission">
  <svg width="30" height="30" viewBox="0 0 24 24" fill="none" stroke="#fff" stroke-width="1.6"><path d="M5 19l4-4M14 4c4 0 6 2 6 6l-7 7-6-6z M9 12l-4 0 3-3h4"/></svg>
  <h3>OUR MISSION</h3>
  <p>To connect people and organizations interests, inspiring each other and enabling together reach better results.</p>
</aside>

<section class="events">
  <h2><svg width="24" height="24" viewBox="0 0 24 24" fill="none" stroke="#333" stroke-width="1.6"><rect x="3" y="5" width="18" height="16"/><path d="M3 10h18M8 3v4M16 3v4M7 14h2M11 14h2M15 14h2M7 17h2M11 17h2"/></svg>UPCOMING EVENTS</h2>
  <article class="event">
    <div class="event-photo" style="background:linear-gradient(90deg,#7b8794,#c9ced4)" role="img" aria-label="Photo of a business meeting at a table"></div>
    <div><small>20 Mar, 2017</small><h5>Lorem ipsum dolor sit amet.</h5><p>Sed do eiusmod tempor incididunt ut labore et dolore magna aliqua. Ut enim ad minim veniam.</p></div>
  </article>
  <article class="event">
    <div class="event-photo" style="background:linear-gradient(135deg,#0e2a52,#2e6fb4)" role="img" aria-label="Photo of hands holding a glowing network of people"></div>
    <div><small>20 Mar, 2017</small><h5>Lorem ipsum dolor sit amet.</h5><p>Sed do eiusmod tempor incididunt ut labore et dolore magna aliqua. Ut enim ad minim veniam.</p></div>
  </article>
  <article class="event" style="border-bottom:none">
    <div class="event-photo" style="background:linear-gradient(90deg,#9aa3ad,#d8dbe0)" role="img" aria-label="Photo of colleagues discussing documents"></div>
    <div><small>20 Mar, 2017</small><h5>Lorem ipsum dolor sit amet.</h5><p>Sed do eiusmod tempor incididunt ut labore et dolore magna aliqua. Ut enim ad minim veniam.</p></div>
  </article>
  <span class="btn">View events</span>
</section>

<section class="agency">
  <h2 class="agency-head">Velmorix is the first crowdsourced IT recruitment agency</h2>
  <p class="agency-lead">We have deep and unquie expertise in IT area using crowdsourcing to search the best market candidates faster than ever.</p>
  <div class="feature" style="left:20px;top:158px">
    <svg viewBox="0 0 40 40" fill="none" stroke="var(--blue)" stroke-width="2"><path d="M32 20a12 12 0 11-4-9"/><path d="M29 5v7h-7"/></svg>
    <h6>END-TO-END</h6><p>IT recruitment focused on result</p>
  </div>
  <div class="feature" style="left:266px;top:158px">
    <svg viewBox="0 0 40 40" fill="none" stroke="var(--blue)" stroke-width="2"><circle cx="20" cy="20" r="15"/><circle cx="20" cy="15" r="4"/><path d="M12 28c2-6 14-6 16 0"/></svg>
    <h6>EASY</h6><p>One point of contact to the recruiters crowd</p>
  </div>
  <div class="feature" style="left:20px;top:320px">
    <svg viewBox="0 0 40 40" fill="none" stroke="var(--blue)" stroke-width="2"><path d="M8 15l6-7h12l6 7-12 16z M8 15h24"/></svg>
    <h6>QUALITY</h6><p>Broad and deep expertize in all IT areas</p>
  </div>
  <div class="feature" style="left:266px;top:320px">
    <svg viewBox="0 0 40 40" fill="none" stroke="var(--blue)" stroke-width="2"><rect x="9" y="6" width="22" height="28" rx="2"/><circle cx="20" cy="20" r="6"/><path d="M20 16v4l3 2"/></svg>
    <h6>FASTER</h6><p>Network gives result in 3 days</p>
  </div>
</section>

<section class="how">
  <div class="how-frame"></div>
  <span class="how-mark"></span>
  <h2>HOW DOES IT WORK?</h2>
  <p>Watch this video to learn about our process and results you can expect.</p>
  <div class="video-back"></div>
  <div class="photo video" role="img" aria-label="Video still of a businesswoman in an office"></div>
  <span class="play"></span>
</section>

<section class="lower">
  <div class="panel-head" style="left:73px;top:50px;width:514px;background:var(--purple)">
    <svg width="22" height="22" viewBox="0 0 24 24" fill="none" stroke="#fff" stroke-width="1.8"><path d="M3 4h14v10H8l-5 4z M19 8h2v10l-4-3h-6"/></svg>TESTIMONIALS<span class="more">VIEW MORE</span>
  </div>
  <div class="photo testi-photo" role="img" aria-label="Photo of a smiling woman at a desk"></div>
  <div class="quote">
    <div class="mark">&ldquo;</div>
    <p>Lorem ipsum dolor sit amet, consectetur adipiscing elit, sed do eiusmod tempor incididunt ut labore et dolore magna aliqua. Ut enim ad minim veniam, quis nostrud exercitation ullamco laboris nisi ut aliquip ex ea commodo consequat. Duis aute irure.</p>
    <b>- Arlen Fosbury</b>
  </div>
  <span class="arrow" style="left:110px">&#8249;</span>
  <span class="arrow" style="left:428px">&#8250;</span>

  <div class="panel-head" style="left:617px;top:50px;width:510px;background:var(--green)">
    <svg width="22" height="22" viewBox="0 0 24 24" fill="#fff"><path d="M3 9h4l9-5v16l-9-5H3z"/></svg>FROM THE BLOG<span class="more">VIEW MORE</span>
  </div>
  <div class="blog">
    <article class="post"><div class="post-photo" style="background:linear-gradient(135deg,#9ab8d6,#e6eef6)" role="img" aria-label="Illustration of a connected network"></div><div><small>06 Mar, 2017</small><h5>Lorem ipsum dolor sit amet, consec tetur adipiscing elit,</h5></div></article>
    <article class="post"><div class="post-photo" style="background:linear-gradient(90deg,#8d96a0,#d4d7db)" role="img" aria-label="Photo of people in a job interview"></div><div><small>06 Mar, 2017</small><h5>Lorem ipsum dolor sit amet, consec tetur adipiscing elit,</h5></div></article>
    <article class="post"><div class="post-photo" style="background:linear-gradient(90deg,#6f7a86,#b8bec5)" role="img" aria-label="Photo of a handshake across a desk"></div><div><small>06 Mar, 2017</small><h5>Lorem ipsum dolor sit amet, consec tetur adipiscing elit,</h5></div></article>
  </div>
</section>

<footer class="site-footer">
  <h4 class="col-title" style="left:73px">QUICK LINKS</h4>
  <ul class="links"><li>Home</li><li>About Us</li><li>Products</li><li>News</li><li>Contacts</li></ul>
  <h4 class="col-title" style="left:204px">CONTACT INFORMATION</h4>
  <div class="contact">
    <p>Lindenova ul. 48, Brezhino village, Ostrovsky District, Moscow Region, 142117, Russia</p>
    <p style="margin-top:16px">+7 (495) 000 1 234</p>
    <p style="margin-top:16px">info@velmorix-hire.ru</p>
  </div>
  <h4 class="col-title" style="left:478px">SUBSCRIBE NEWSLETTER</h4>
  <div class="newsletter">
    <p style="margin-bottom:14px">Enter your email and receive latest offers &amp; news updates!</p>
    <div class="field">Name</div>
    <div class="field">Email</div>
    <span class="subscribe">SUBSCRIBE</span>
  </div>
  <div class="follow">FOLLOW US: <span class="circle"></span><span class="circle"></span></div>
  <div class="foot-brand"><span class="brand-dot"></span><span class="brand-name">velmorix</span></div>
  <p class="copy">&copy; 2017 Velmorix Crowd Recruitment .<br>Terms of Use &nbsp;|&nbsp; Privacy Policy</p>

  <form class="feedback">
    <span class="feedback-tab"></span>
    <h3>FEEDBACK</h3>
    <div class="field">Name</div>
    <div class="field">Email</div>
    <div class="field message">Message</div>
    <span class="send">SUBMIT</span>
  </form>
</footer>

</body>
</html>
```